BrightMesa Business Card Contest

We are looking for a modern business card that catches attention and is unique. Attached is the brand guide and logo files. Please note that the back side (not the side with our name and info) with be UV raise printed, so have fun with the design there. We want to include Name, Title, Phone number, email, website.

Contact Information for Business Card

Please see project description

```html
<!DOCTYPE html>
<html lang="en">
<head>
<meta charset="utf-8">
<title>BrightMesa Business Card</title>
<link href="https://fonts.googleapis.com/css2?family=Outfit:wght@300;400;700&display=swap" rel="stylesheet">
<style>
  :root {
    --stage: #2a2a2c;
    --card: #161616;
    --card-edge: #0c0c0c;
    --white: #ffffff;
    --red: #e0281e;
    --pattern-light: #d9d9d9;
    --pattern-mid: #555555;
    --pattern-dark: #121212;
  }
  * { margin: 0; padding: 0; box-sizing: border-box; }
  html, body { width: 1200px; height: 900px; overflow: hidden; }
  body {
    background: var(--stage);
    font-family: "Outfit", sans-serif;
    position: relative;
  }
  .card {
    position: absolute;
    background: var(--card);
    border-radius: 26px;
    box-shadow: 0 18px 40px rgba(0,0,0,.45);
    overflow: hidden;
  }
  /* Back side (UV raised pattern) */
  .card-back {
    left: 110px; top: 170px;
    width: 320px; height: 560px;
  }
  .uv-pattern {
    position: absolute; inset: 0;
    background: linear-gradient(180deg, var(--pattern-light) 0%, var(--pattern-mid) 38%, var(--pattern-dark) 75%, var(--card-edge) 100%);
  }
  .back-wordmark {
    position: absolute;
    left: 0; right: 0; top: 250px;
    display: flex; align-items: center; justify-content: center; gap: 10px;
    color: var(--white);
    font-size: 34px; font-weight: 400;
    letter-spacing: .5px;
  }
  .brand-square {
    width: 16px; height: 16px;
    background: var(--white);
  }
  /* Front side (name and contact) */
  .card-front {
    left: 520px; top: 300px;
    width: 580px; height: 330px;
  }
  .front-wordmark {
    position: absolute;
    left: 48px; top: 138px;
    display: flex; align-items: center; gap: 10px;
    color: var(--white);
    font-size: 40px; font-weight: 400;
    letter-spacing: .5px;
  }
  .divider {
    position: absolute;
    left: 306px; top: 80px;
    width: 1.5px; height: 170px;
    background: var(--red);
  }
  .details {
    position: absolute;
    left: 330px; top: 96px;
  }
  .person-name {
    color: var(--red);
    font-size: 30px; font-weight: 700;
    line-height: 1.05;
  }
  .person-title {
    color: var(--white);
    font-size: 16px; font-weight: 300;
    letter-spacing: .6px;
    margin-bottom: 16px;
  }
  .contact-list { list-style: none; }
  .contact-list li {
    display: flex; align-items: center; gap: 9px;
    color: var(--white);
    font-size: 16px; font-weight: 300;
    letter-spacing: .4px;
    line-height: 1.6;
  }
  .contact-list svg { width: 14px; height: 14px; fill: var(--red); flex: none; }
</style>
</head>
<body>

<section class="card card-back" aria-label="Card back">
  <div class="uv-pattern" role="img" aria-label="Raised UV gloss pattern of repeating brand shapes fading from light grey to black"></div>
  <div class="back-wordmark"><span class="brand-square"></span>BrightMesa</div>
</section>

<section class="card card-front" aria-label="Card front">
  <div class="front-wordmark"><span class="brand-square"></span>BrightMesa</div>
  <div class="divider"></div>
  <div class="details">
    <h1 class="person-name">Daniel Hartley</h1>
    <p class="person-title">Managing Director</p>
    <ul class="contact-list">
      <li>
        <svg viewBox="0 0 24 24" aria-hidden="true"><path d="M6.6 10.8a15 15 0 0 0 6.6 6.6l2.2-2.2c.3-.3.7-.4 1-.2 1.1.4 2.3.6 3.6.6.6 0 1 .4 1 1V20c0 .6-.4 1-1 1A17 17 0 0 1 3 4c0-.6.4-1 1-1h3.5c.6 0 1 .4 1 1 0 1.3.2 2.5.6 3.6.1.3 0 .7-.2 1z"/></svg>
        123 456 789
      </li>
      <li>
        <svg viewBox="0 0 24 24" aria-hidden="true"><path d="M2 5h20v14H2z M2 5l10 8 10-8" /></svg>
        info@brightmesa.com
      </li>
      <li>
        <svg viewBox="0 0 24 24" aria-hidden="true"><circle cx="12" cy="12" r="10"/></svg>
        www.brightmesa.com
      </li>
    </ul>
  </div>
</section>

</body>
</html>
```